Interior Styling Workshop needs a brochure designed.

Hue Harbor is an interior design firm based in Sydney. We will be running Interior Styling Workshops
for all people interested in learning how to decorate
their home. It is important to show modern interior images to attract and excite their creative juices!
Colours we would like is a dark charcoal background
with Chartreuse trim for our logo and for the brochure.
We have attached some of our ideas on wording.
Our images can be replaced or changed to suit your
design.
The final design should be very stylish and to instill a desire to attend our workshops!

Target Market(s)

Mainly female adults in Sydney, aged approx. 25 to 60, who are interested in
interior decorating their homes.

Industry/Entity Type

Learning

Colors
5c5c5c
acd036

Requirements
Must have
• Must show good visual images to catch attention.
Nice to have
• Page layout i.e. to uploaded document, but open to any designs that work better.

```html
<!DOCTYPE html>
<html lang="en">
<head>
<meta charset="utf-8">
<title>Hue Harbor – Interior Styling Workshop Brochure</title>
<link href="https://fonts.googleapis.com/css2?family=Open+Sans:wght@400;600&family=Arimo:ital,wght@0,400;0,700;1,400&display=swap" rel="stylesheet">
<style>
:root{
  --charcoal:#5c5c5c;
  --charcoal-deep:#4a4a4c;
  --chartreuse:#acd036;
  --paper:#ffffff;
  --paper-soft:#f4f4f2;
  --stage:#e6e6e4;
  --ink:#3a3a3a;
  --head:"Open Sans",sans-serif;
  --body:"Arimo",sans-serif;
}
*{box-sizing:border-box;margin:0;padding:0}
html,body{width:1200px;height:1152px;overflow:hidden}
body{background:var(--stage);position:relative;font-family:var(--body);color:var(--ink)}
.abs{position:absolute}
.spread{position:absolute;left:60px;width:692px;box-shadow:0 2px 8px rgba(0,0,0,.25);background:var(--paper)}
.spread--outside{top:15px;height:542px}
.spread--inside{top:583px;height:540px}
.photo{position:absolute}
.photo--bedroom{background:linear-gradient(90deg,#2f2522 0%,#4a3a33 14%,#6fa9aa 28%,#9fcfcf 42%,#e9e6dc 55%,#f1ece2 63%,#b08a5c 75%,#d8c7a6 86%,#8e7a62 100%)}
.photo--lounge-front{background:linear-gradient(180deg,#f7f7f5 0%,#f1f0ec 30%,#e6e8dd 52%,#f4f3ef 66%,#d9c8ab 80%,#b8966a 100%)}
.photo--living-small{background:linear-gradient(180deg,#dcdfe0 0%,#eef0ef 35%,#d6d6cf 58%,#5a5a5c 78%,#3e3e40 100%)}
.photo--open-plan{background:linear-gradient(180deg,#e6e1d6 0%,#d9cfbf 35%,#7d6e62 58%,#a8743f 78%,#8a5a2e 100%)}
.photo--dining{background:linear-gradient(180deg,#ece9e2 0%,#cfc7ba 38%,#5b5650 60%,#a87745 82%,#7d5430 100%)}
.photo--white-lounge{background:linear-gradient(180deg,#fbfbfa 0%,#f3f3f1 45%,#e2e2df 70%,#8a8a88 86%,#2d2d2e 100%)}
.band-dark{background:var(--charcoal-deep)}
.band-green{background:var(--chartreuse)}
.brand{display:flex;align-items:center;gap:8px;justify-content:center;font-family:var(--head);font-weight:600;color:var(--charcoal-deep)}
.brand__mark{width:14px;height:14px;background:var(--chartreuse);flex:none}
.panel-title{font-family:var(--head);color:var(--charcoal-deep);text-align:center;line-height:1.05}
.tagline{font-family:var(--head);color:#fff;text-align:center;font-size:19px;line-height:1.15}
.copy{font-size:10px;line-height:13.5px;color:#fff;text-align:justify;hyphens:auto;-webkit-hyphens:auto;word-spacing:-0.3px}
.copy .hl{color:var(--chartreuse)}
.questions{font-size:10.6px;line-height:14px;color:#fff;text-align:justify;hyphens:auto;-webkit-hyphens:auto}
.questions p{margin-bottom:14px}
.questions strong{color:var(--chartreuse)}
.learn h3{font-size:11px;color:var(--chartreuse);font-weight:700;margin-bottom:2px}
.learn li{list-style:none;font-size:9.2px;line-height:12px;color:#fff;padding-left:13px;position:relative}
.learn li svg{position:absolute;left:0;top:2px}
.learn .extra{margin-top:10px;font-size:9px;line-height:12px;color:var(--chartreuse);font-style:italic}
.details{text-align:center;color:var(--chartreuse);font-size:12.5px;line-height:12px}
.details p{margin-bottom:10px}
.footer-contact{position:absolute;display:flex;align-items:center;gap:4px;color:#222;font-size:17px}
.footer-contact--web{font-size:11px}
</style>
</head>
<body>

<section class="spread spread--outside">
  <div class="photo photo--bedroom" role="img" aria-label="Modern bedroom with dark timber bed, turquoise feature wall and hanging wicker chair" style="left:0;top:0;width:462px;height:160px"></div>
  <div class="abs band-dark" style="left:0;top:160px;width:462px;height:355px"></div>

  <div class="abs" style="left:77px;top:188px;width:100px;height:118px;background:#fbfbf4"></div>
  <p class="abs copy" lang="en" style="left:45px;top:320px;width:164px">Tessa Marlow and Nadia Price of <span class="hl">HUE HARBOR</span> Interior Design understand the frustration and confusion that D.I.Y. home decorators face and will be holding <span class="hl">INTERIOR STYLING WORKSHOPS</span> in which you will learn how to create innovative colour schemes and styles from concept to completion in a fun, hands on experience, surrounded by beautiful furniture, fabrics, soft furnishings and home wares that will get your creative juices flowing!</p>

  <div class="abs questions" lang="en" style="left:262px;top:182px;width:171px">
    <p>Would you like to transform your home?</p>
    <p>Do you feel <strong>OVERWHELMED</strong> and <strong>CONFUSED</strong> as to Where to start?</p>
    <p>Are you unsure of a colour scheme, what type of furniture, Soft furnishings, accessories suit your home and lifestyle?</p>
    <p>Where to buy? What will suit your budget?</p>
  </div>
  <div class="photo photo--living-small" role="img" aria-label="Bright living room with white sofa, dark rug and yellow accents" style="left:260px;top:396px;width:173px;height:99px"></div>

  <div class="abs" style="left:462px;top:0;width:230px;height:440px;background:var(--paper-soft)"></div>
  <div class="abs brand" style="left:462px;top:95px;width:230px;font-size:25px"><span class="brand__mark"></span>Hue Harbor</div>
  <div class="abs panel-title" style="left:462px;top:170px;width:230px;font-size:20px">INTERIOR STYLING<br>WORKSHOP</div>
  <div class="photo photo--lounge-front" role="img" aria-label="White living room with sofa, green cushions, coffee table and potted tree on timber floor" style="left:462px;top:215px;width:230px;height:225px"></div>
  <div class="abs band-dark" style="left:462px;top:440px;width:230px;height:75px"></div>
  <div class="abs tagline" style="left:462px;top:456px;width:230px">FIND YOUR STYLE,<br>BE INSPIRED</div>
  <div class="abs band-green" style="left:0;top:515px;width:692px;height:27px"></div>
</section>

<section class="spread spread--inside">
  <div class="photo photo--open-plan" role="img" aria-label="Open plan lounge and dining room with timber floors" style="left:0;top:0;width:229px;height:134px"></div>
  <div class="abs band-dark" style="left:0;top:134px;width:229px;height:365px"></div>
  <div class="abs learn" style="left:34px;top:151px;width:170px">
    <h3>YOU WILL LEARN</h3>
    <ul>
      <li><svg width="9" height="8" viewBox="0 0 9 8"><path d="M1 4l2.5 3L8 1" stroke="#acd036" stroke-width="1.4" fill="none"/></svg>Where and how to use colour, shape, form, and different textures to create a balanced and harmonious environment.</li>
      <li><svg width="9" height="8" viewBox="0 0 9 8"><path d="M1 4l2.5 3L8 1" stroke="#acd036" stroke-width="1.4" fill="none"/></svg>Current styles and what inspires you.</li>
      <li><svg width="9" height="8" viewBox="0 0 9 8"><path d="M1 4l2.5 3L8 1" stroke="#acd036" stroke-width="1.4" fill="none"/></svg>Space planning and furniture placement for your room to give a balanced and spacious feel.</li>
      <li><svg width="9" height="8" viewBox="0 0 9 8"><path d="M1 4l2.5 3L8 1" stroke="#acd036" stroke-width="1.4" fill="none"/></svg>Where to start!</li>
      <li><svg width="9" height="8" viewBox="0 0 9 8"><path d="M1 4l2.5 3L8 1" stroke="#acd036" stroke-width="1.4" fill="none"/></svg>How to bring it all together with the finishing touches.</li>
      <li><svg width="9" height="8" viewBox="0 0 9 8"><path d="M1 4l2.5 3L8 1" stroke="#acd036" stroke-width="1.4" fill="none"/></svg>Why Concept plans and mood boards are important.</li>
    </ul>
    <p class="extra">You will also enjoy making your very own mood board which will give you insight and inspire you to commence your project with confidence.</p>
  </div>
  <div class="photo photo--living-small" role="img" aria-label="Bright living room with white sofa, dark rug and yellow accents" style="left:33px;top:392px;width:174px;height:97px"></div>

  <div class="abs" style="left:229px;top:0;width:229px;height:499px;background:var(--paper-soft)"></div>
  <div class="abs" style="left:247px;top:32px;width:193px;height:431px;border:2px solid var(--chartreuse)"></div>
  <div class="abs panel-title" style="left:247px;top:44px;width:193px;font-size:16.5px">INTERIOR STYLING<br>WORKSHOP</div>
  <div class="abs brand" style="left:247px;top:142px;width:193px;font-size:21px"><span class="brand__mark"></span>Hue Harbor</div>
  <div class="abs panel-title" style="left:247px;top:224px;width:193px;font-size:17px">FIND YOUR STYLE,<br>BE INSPIRED</div>
  <p class="abs" style="left:247px;top:284px;width:193px;text-align:center;font-size:12.5px;line-height:12.5px;color:var(--charcoal-deep)">For More Information,<br>Dates, Times And Venues Of<br>Upcoming Workshops.</p>
  <p class="abs" style="left:247px;top:349px;width:193px;text-align:center;font-size:18px;line-height:19px;color:var(--charcoal-deep)">Please Call Or Visit<br><strong style="color:var(--chartreuse);font-size:21px">TESSA</strong> on</p>
  <div class="abs band-dark" style="left:249px;top:397px;width:190px;height:65px"></div>
  <p class="abs" style="left:249px;top:408px;width:190px;text-align:center;color:var(--chartreuse);font-weight:700;font-size:22px;line-height:22px">0491570156<br><span style="font-size:11.5px;line-height:14px">www.hueharbor.com.au</span></p>

  <div class="photo photo--dining" role="img" aria-label="Dining room with dark chairs opening to a balcony" style="left:458px;top:0;width:234px;height:114px"></div>
  <div class="abs band-dark" style="left:458px;top:114px;width:234px;height:155px"></div>
  <div class="abs details" style="left:458px;top:137px;width:234px">
    <p>All Materials and Lunch<br>are provided.</p>
    <p>Bookings are essential.</p>
    <p>Numbers are limited to <span style="color:#fff;font-weight:700;font-size:21px">10</span> per<br>workshop</p>
    <p style="color:#fff;font-style:italic;font-size:14px;margin-top:14px">Cost: <strong style="color:var(--chartreuse);font-style:normal">$240</strong> (including lunch)</p>
  </div>
  <div class="photo photo--white-lounge" role="img" aria-label="Minimal white lounge with black leather armchair, glass table and bamboo plant" style="left:458px;top:269px;width:234px;height:230px"></div>

  <div class="abs band-green" style="left:0;top:499px;width:692px;height:41px"></div>
  <div class="footer-contact" style="left:48px;top:508px">
    <svg width="17" height="17" viewBox="0 0 18 18"><circle cx="9" cy="9" r="8" fill="none" stroke="#222" stroke-width="1.3"/><path d="M6 4.5l2 2.2-1 1.2c.6 1.3 1.5 2.2 2.8 2.8l1.2-1 2.2 2-1.3 1.6C8.4 13 5 9.6 4.5 5.8z" fill="#222"/></svg>0491570156</div>
  <div class="footer-contact footer-contact--web" style="left:258px;top:512px">
    <svg width="14" height="14" viewBox="0 0 14 14" fill="none" stroke="#222" stroke-width="1"><circle cx="7" cy="7" r="6"/><ellipse cx="7" cy="7" rx="2.6" ry="6"/><path d="M1 7h12M2 4h10M2 10h10"/></svg>www.hueharbor.com.au</div>
  <div class="footer-contact" style="left:510px;top:508px">
    <svg width="17" height="17" viewBox="0 0 18 18"><circle cx="9" cy="9" r="8" fill="none" stroke="#222" stroke-width="1.3"/><path d="M6 4.5l2 2.2-1 1.2c.6 1.3 1.5 2.2 2.8 2.8l1.2-1 2.2 2-1.3 1.6C8.4 13 5 9.6 4.5 5.8z" fill="#222"/></svg>0491570156</div>
</section>

</body>
</html>
```